New stationary design for online film company

We need some new stationary to fit with our new logo. The stationary should be professional, clean and simple.
We need designs for a full set of business stationary.
We need - letterhead, envelopes, invoices, proposals, coverslip/note and cover page

Industry/Entity Type

Business

```html
<!DOCTYPE html>
<html lang="en">
<head>
<meta charset="utf-8">
<title>Reelwave Stationery Set</title>
<link href="https://fonts.googleapis.com/css2?family=Source+Sans+3:wght@400;600;700&family=Great+Vibes&display=swap" rel="stylesheet">
<style>
  :root {
    --bg: #e3e5e8;
    --paper: #f7f8fa;
    --navy: #22507a;
    --sky: #8fb3d6;
    --ink: #4a4f55;
    --ink-soft: #6f757c;
    --ghost: #e6e8eb;
    --edge: #cfd3d8;
  }
  * { box-sizing: border-box; margin: 0; padding: 0; }
  html, body { width: 1200px; height: 797px; overflow: hidden; }
  body {
    background: var(--bg);
    font-family: "Source Sans 3", sans-serif;
    color: var(--ink);
    position: relative;
  }
  .sheet {
    position: absolute;
    background: var(--paper);
    box-shadow: 0 1px 0 var(--edge), 0 8px 18px rgba(0,0,0,0.08);
    overflow: hidden;
  }
  .brand {
    display: flex;
    align-items: center;
    gap: 6px;
    font-weight: 600;
    color: var(--navy);
    letter-spacing: 0.2px;
  }
  .brand-dot {
    border-radius: 50%;
    background: var(--navy);
    flex: none;
  }
  .ghost-circle {
    position: absolute;
    border-radius: 50%;
    background: var(--ghost);
  }

  /* Letterhead */
  .letterhead { left: 40px; top: 45px; width: 500px; height: 707px; }
  .letterhead .brand { position: absolute; left: 44px; top: 52px; font-size: 26px; }
  .letterhead .brand-dot { width: 18px; height: 18px; }
  .letterhead .ghost-circle { width: 250px; height: 250px; right: -40px; top: 250px; }
  .letter-body {
    position: absolute; left: 96px; top: 130px; width: 330px;
    font-size: 8.6px; line-height: 1.5; color: var(--ink);
  }
  .letter-greeting { font-weight: 700; margin-bottom: 10px; }
  .letter-body p { margin-bottom: 10px; }
  .signature {
    font-family: "Great Vibes", cursive;
    font-size: 30px; color: #2b2f34; margin-top: 18px; line-height: 1;
  }
  .signature-role { font-weight: 700; font-size: 8.6px; margin-top: 2px; }
  .letter-footer {
    position: absolute; left: 96px; bottom: 40px;
    display: flex; gap: 14px; font-size: 8.6px; line-height: 1.45;
  }
  .letter-footer .divider { width: 1px; background: var(--ink-soft); }
  .label { display: inline-block; width: 10px; color: var(--ink-soft); }
  .accent { color: var(--navy); font-weight: 600; }

  /* Envelope */
  .envelope { left: 590px; top: 45px; width: 570px; height: 285px; }
  .envelope .brand { position: absolute; left: 30px; top: 26px; font-size: 20px; }
  .envelope .brand-dot { width: 14px; height: 14px; }
  .envelope-address {
    position: absolute; left: 50px; top: 56px;
    font-size: 7.5px; line-height: 1.4; color: var(--ink);
  }
  .envelope .ghost-circle { width: 170px; height: 170px; right: 40px; bottom: -50px; }

  /* Business cards */
  .card { width: 270px; height: 160px; top: 400px; }
  .card-front { left: 590px; background: var(--navy); }
  .card-front .brand { position: absolute; left: 0; right: 0; top: 56px; justify-content: center; color: #fff; font-size: 24px; }
  .card-front .brand-dot { background: #fff; width: 16px; height: 16px; }
  .card-tagline {
    position: absolute; left: 0; right: 0; top: 94px; text-align: center;
    font-size: 8px; letter-spacing: 1.2px; color: var(--sky);
  }
  .card-back { left: 890px; border-left: 8px solid var(--navy); }
  .card-back .brand { position: absolute; left: 18px; top: 20px; font-size: 18px; }
  .card-back .brand-dot { width: 12px; height: 12px; }
  .card-person { position: absolute; left: 18px; top: 56px; }
  .card-name { font-weight: 700; font-size: 10px; color: #2b2f34; }
  .card-title { font-size: 7.5px; color: var(--ink-soft); }
  .card-web { position: absolute; left: 18px; bottom: 22px; font-size: 7.5px; color: var(--navy); }
  .card-contact {
    position: absolute; right: 16px; top: 70px;
    font-size: 7.5px; line-height: 1.45; color: var(--ink);
  }
</style>
</head>
<body>

  <section class="sheet letterhead" aria-label="Letterhead">
    <div class="ghost-circle" aria-hidden="true"></div>
    <div class="brand"><span class="brand-dot"></span>reelwave</div>
    <div class="letter-body">
      <p class="letter-greeting">Lorem Ipsum,</p>
      <p>Cras mattis consectetur purus sit amet fermentum. Etiam porta sem malesuada magna mollis euismod. Integer posuere erat a ante venenatis dapibus posuere velit aliquet. Cras justo odio, dapibus ac facilisis in, egestas eget quam. Aenean eu leo quam. Pellentesque ornare sem lacinia quam venenatis vestibulum.</p>
      <p>Vivamus sagittis lacus vel augue laoreet rutrum faucibus dolor auctor. Donec sed odio dui. Etiam porta sem malesuada magna mollis euismod. Morbi leo risus, porta ac consectetur ac, vestibulum at eros. Nullam id dolor id nibh ultricies vehicula ut id elit.</p>
      <p>Donec id elit non mi porta gravida at eget metus. Fusce dapibus, tellus ac cursus commodo, tortor mauris condimentum nibh, ut fermentum massa justo sit amet risus. Cras justo odio, dapibus ac facilisis in, egestas eget quam. Cum sociis natoque penatibus et magnis dis parturient montes, nascetur ridiculus mus.</p>
      <p>Cum sociis natoque penatibus et magnis dis parturient montes, nascetur ridiculus mus. Curabitur blandit tempus porttitor. Aenean lacinia bibendum nulla sed consectetur. Lorem ipsum dolor sit amet, consectetur adipiscing elit.</p>
      <p>Cras justo odio, dapibus ac facilisis in, egestas eget quam. Morbi leo risus, porta ac consectetur ac, vestibulum at eros. Integer posuere erat a ante venenatis dapibus posuere velit aliquet.</p>
      <div class="signature">Your Name</div>
      <div class="signature-role">Company Director</div>
    </div>
    <footer class="letter-footer">
      <div>
        <div><span class="label">t</span>917-555-0142</div>
        <div><span class="label">m</span>123-555-0190</div>
        <div><span class="label">e</span>mira@reelwave.tv</div>
      </div>
      <div class="divider"></div>
      <div>
        <div>58 Harbor Lane Suite 12</div>
        <div>Brooklyn NY 11201 USA</div>
        <div>www.<span class="accent">reelwave</span>.tv</div>
      </div>
    </footer>
  </section>

  <section class="sheet envelope" aria-label="Envelope">
    <div class="ghost-circle" aria-hidden="true"></div>
    <div class="brand"><span class="brand-dot"></span>reelwave</div>
    <div class="envelope-address">
      <div>58 Harbor Lane Suite 12</div>
      <div>Brooklyn NY 11201 USA</div>
      <div>www.<span class="accent">reelwave</span>.tv</div>
    </div>
  </section>

  <section class="sheet card card-front" aria-label="Business card front">
    <div class="brand"><span class="brand-dot"></span>reelwave</div>
    <div class="card-tagline">ONLINE FILM PRODUCTION &amp; STRATEGY</div>
  </section>

  <section class="sheet card card-back" aria-label="Business card back">
    <div class="brand"><span class="brand-dot"></span>reelwave</div>
    <div class="card-person">
      <div class="card-name">Mira Delacroix</div>
      <div class="card-title">Manager</div>
    </div>
    <div class="card-web">www.reelwave.tv</div>
    <div class="card-contact">
      <div><span class="label">t</span>917-555-0142</div>
      <div><span class="label">m</span>123-555-0190</div>
      <div><span class="label">e</span>mira@reelwave.tv</div>
      <div>58 Harbor Lane Suite 12</div>
      <div>Brooklyn NY 11201 USA</div>
    </div>
  </section>

</body>
</html>
```